Letterhead Design for Law Firm that Specializes in Property Damage Litigation

We are looking for a redesign of our letterhead. Our current letterhead lists all of our current staff members and we'd like to come up with a design that does NOT list all of the staff members so that it does not need to be updated with every newly hired employee. Must be in editable format.

We are a law firm that specializes in property damage, so we need something that is professional, yet modern. The final design should use our existing logo and should use a blue color scheme (alternate colors would be gray, black, and white).

Industry/Entity Type

Legal

Colors
0054AA
0677BA
7BADD7
CADEEF
E8F1F8

```html
<!DOCTYPE html>
<html lang="en">
<head>
<meta charset="utf-8">
<title>Harlow Kessing &amp; Marrow — Letterhead</title>
<link rel="stylesheet" href="https://fonts.googleapis.com/css2?family=Arimo:wght@400;700&family=Didact+Gothic&family=Questrial&display=swap">
<style>
  :root {
    --navy: #0a3266;
    --ink: #555555;
    --rule-gray: #666666;
    --page: #ffffff;
    --backdrop: #dedede;
    --sig: #e6e6e6;
  }
  * { box-sizing: border-box; margin: 0; padding: 0; }
  html, body { width: 1189px; height: 1200px; overflow: hidden; }
  body { background: var(--backdrop); font-family: "Arimo", Arial, sans-serif; }

  .letterhead {
    position: absolute; left: 191px; top: 30px;
    width: 806px; height: 1140px;
    background: var(--page);
    box-shadow: 3px 4px 8px rgba(0,0,0,.25);
    overflow: hidden;
  }

  .firm-name {
    position: absolute; left: 42px; top: 48px;
    display: flex; align-items: center; gap: 12px;
  }
  .firm-name__mark { width: 14px; height: 14px; background: var(--navy); }
  .firm-name__text {
    color: var(--navy); font-weight: 700; font-size: 22px;
    line-height: 25px; letter-spacing: 1.5px; text-transform: uppercase;
  }

  .office { position: absolute; top: 49px; font-size: 11.6px; line-height: 15px; color: var(--ink); }
  .office--pa { right: 272px; text-align: right; }
  .office--nj { left: 560px; }
  .office__title { color: var(--navy); font-weight: 700; font-size: 11.8px; margin-bottom: 5px; }
  .office__contacts { margin-top: 3px; display: flex; gap: 12px; }
  .office--pa .office__contacts { justify-content: flex-end; }
  .contact { display: inline-flex; align-items: center; gap: 3px; }
  .contact svg { width: 9px; height: 9px; fill: var(--navy); }
  .office-divider { position: absolute; left: 547px; top: 50px; width: 1px; height: 66px; background: var(--ink); }

  .letter { position: absolute; left: 72px; top: 350px; width: 632px; color: var(--ink); }
  .letter__greeting { font-family: "Questrial", sans-serif; font-weight: 700; font-size: 17.5px; margin-bottom: 28px; -webkit-text-stroke: .3px var(--ink); }
  .letter__body p { font-size: 12.8px; line-height: 16.4px; margin-bottom: 14.5px; }
  .letter__closing { font-family: "Didact Gothic", sans-serif; font-size: 10px; font-weight: 700; margin-top: 23px; -webkit-text-stroke: .3px var(--ink); }
  .letter__signature { width: 132px; height: 38px; margin-top: 35px; background: var(--sig); border-radius: 3px; }

  .footer-rule { position: absolute; left: 0; right: 0; top: 1091px; height: 7px; background: var(--rule-gray); }
  .footer-band {
    position: absolute; left: 0; right: 0; top: 1102px; height: 38px;
    background: var(--navy); color: #fff;
    display: flex; align-items: center; justify-content: center;
    padding-left: 34px;
    font-weight: 700; font-size: 12.5px; letter-spacing: 8.5px;
  }
</style>
</head>
<body>
  <main class="letterhead">
    <header>
      <div class="firm-name">
        <span class="firm-name__mark"></span>
        <div class="firm-name__text">Harlow<br>Kessing &amp;<br>Marrow</div>
      </div>

      <section class="office office--pa">
        <h2 class="office__title">PHILADELPHIA OFFICE</h2>
        <p>2200 Market Street, Suite 840</p>
        <p>Philadelphia, PA 19107</p>
        <p class="office__contacts">
          <span class="contact"><svg viewBox="0 0 10 10"><path d="M2 0.5l2 2-1 1.2c.6 1.3 1.6 2.3 2.9 2.9l1.2-1 2 2-1.3 1.6C4 8.8 1.2 6 0.5 1.8z"/></svg>215.555.0140</span>
          <span class="contact"><svg viewBox="0 0 10 10"><path d="M2.5 0h5v3h-5zM0 3.5h10v4H8V6H2v1.5H0zM2.5 6.5h5V10h-5z"/></svg>&nbsp;215.555.0199</span>
        </p>
      </section>
      <div class="office-divider"></div>
      <section class="office office--nj">
        <h2 class="office__title">NEW JERSEY OFFICE</h2>
        <p>880 Haddon Avenue, Suite 310</p>
        <p>Cherry Hill, NJ 08002</p>
        <p class="office__contacts">
          <span class="contact"><svg viewBox="0 0 10 10"><path d="M2 0.5l2 2-1 1.2c.6 1.3 1.6 2.3 2.9 2.9l1.2-1 2 2-1.3 1.6C4 8.8 1.2 6 0.5 1.8z"/></svg>856.555.0123</span>
          <span class="contact"><svg viewBox="0 0 10 10"><path d="M2.5 0h5v3h-5zM0 3.5h10v4H8V6H2v1.5H0zM2.5 6.5h5V10h-5z"/></svg>&nbsp;215.555.0199</span>
        </p>
      </section>
    </header>

    <article class="letter">
      <p class="letter__greeting">Dear Mr. Smith,</p>
      <div class="letter__body">
        <p>Lorem ipsum dolor sit amet, consectetuer adipiscing elit, sed diam nonmmy nibh euismod tincidunt ut laor eet dolore magna aliquam erat volutpat. Ut wisi enim ad minim veniam, quis nostrud exerci tationmcorper suscipit lobortis nisl ut aliquip ex ea commodo consequat. Duis autem vel eum iriure dolor in hendrerit in vulputate velit esse molestie consequat, vel illum dolore eu feugiat</p>
        <p>Rorem ipsum dolor sit amet, consectetuer adipiscing elit, sed diam nonmmy nibh euismod tincidunt ut laor eet dolore magna aliquam erat volutpat. Ut wisi enim ad minim veniam, quis nostrud exerci tationmcorper suscipit lobortis nisl ut aliquip ex ea commodo consequat. Duis autem vel eum iriure dolor in hendrerit in vulputate velit esse molest</p>
        <p>Dorem ipsum dolor sit amet, consectetuer adipiscing elit, sed diam nonmmy nibh euismod tincidunt ut laor eet dolore magna aliquam erat volutpat. Ut wisi enim ad minim veniam, quis nostrud exerci tationmcorper suscipit lobortis nisl ut aliquip ex ea commodo consequat. Duis autem vel eum iriure dolor in hendrerit in suscipit lobortis nisl ut aliquip ex ea commodo consequat. Duis autem vel eum iriure dolor in hendrerit in vulputate velit esse molestie consequat, vel illum</p>
        <p>Sorem ipsum dolor sit amet, consectetuer adipiscing elit, sed diam nonmmy nibh euismod tincidunt ut laor eet dolore magna aliquam erat volutpat. Ut wisi enim ad minim veniam, quis nostrud exerci tationmcorper suscipit lobortis nisl ut aliquip ex ea commodo consequat. Duis autem vel eum iriure dolor in</p>
      </div>
      <p class="letter__closing">Sincerely,</p>
      <div class="letter__signature" role="img" aria-label="Handwritten signature"></div>
    </article>

    <footer>
      <div class="footer-rule"></div>
      <div class="footer-band">www.hkmlegal.com</div>
    </footer>
  </main>
</body>
</html>
```